Web page design for technology solution company
Velmork Inc.
Dear PH,
Kindly star rate #83 it will help me to go through.
Thanks!
Hi PH,
Any feedback for #52
Thanks
Kindly check your private messages.
#57 and #58 - don't need the extra info. Stick with your earlier versions - like those better. They're simple and not 'overloaded'
#55, #56 - like the simplicity but don't like the dark background
Hi PH, please check your private message. thanks
#13 and #19 - can we see the design without the graphics?
#20 -#24 - much better with the lighter background!
@PH
Kindly check your private message box on the top right & reply asap with your feedback.Thanks
#10 - #12. They seem interesting but on the darker side. Can we see them with a white background?
#9 - Nice and clean design. It's unique and colors are nicely coordinated. Can you find a place for social media icons?
#1 - #5 . Some of the designs look interesting but the background is too dark. Can we see the same with white background?
PH please check your private message
Perin Koldesh

```html
<!DOCTYPE html>
<html lang="en">
<head>
<meta charset="utf-8">
<title>Velmork Inc. – About Us</title>
<link href="https://fonts.googleapis.com/css2?family=Comfortaa:wght@400&family=Oswald:wght@500&family=Arimo:wght@400&display=swap" rel="stylesheet">
<style>
  :root {
    --header-top: #393b3f;
    --header-bottom: #25272a;
    --content-bg: #1d1e20;
    --footer-bg: #2a2b2e;
    --divider: #3c3e42;
    --accent: #b7d636;
    --ribbon-light: #a6d83e;
    --ribbon-dark: #4c8a13;
    --heading: #e6e6e6;
    --body-text: #8f9194;
    --footer-text: #66686b;
    --icon-bg: #505256;
  }
  * { margin: 0; padding: 0; box-sizing: border-box; }
  html, body { width: 1200px; height: 643px; overflow: hidden; background: var(--content-bg); }
  .page { position: relative; width: 1200px; height: 643px; font-family: "Arimo", Arial, sans-serif; }

  .site-header {
    position: absolute; left: 0; top: 0; width: 1200px; height: 216px;
    background:
      repeating-linear-gradient(90deg, rgba(255,255,255,0.018) 0 2px, transparent 2px 5px),
      linear-gradient(180deg, var(--header-top), var(--header-bottom));
    border-bottom: 1px solid #141517;
  }
  .brand {
    position: absolute; left: 0; right: 0; top: 52px;
    display: flex; justify-content: center; align-items: center; gap: 18px;
  }
  .brand-dot { width: 48px; height: 48px; border-radius: 50%; background: var(--accent); }
  .brand-name { font-family: "Comfortaa", sans-serif; font-size: 56px; color: var(--accent); letter-spacing: 1px; }

  .spotlight {
    position: absolute; left: 200px; top: 150px; width: 230px; height: 90px;
    background: radial-gradient(ellipse at 50% 60%, rgba(255,255,255,0.22), rgba(255,255,255,0) 70%);
  }

  .content {
    position: absolute; left: 0; top: 217px; width: 1200px; height: 361px;
    background: var(--content-bg);
  }
  .section-ribbon { position: absolute; left: 252px; top: -25px; }
  .section-ribbon text { font-family: "Oswald", sans-serif; font-size: 21px; fill: #fff; letter-spacing: 0.5px; }

  .about {
    position: absolute; left: 403px; top: 22px; width: 725px;
  }
  .about h2 {
    font-family: "Oswald", sans-serif; font-weight: 500; font-size: 15px;
    color: var(--heading); letter-spacing: 0.5px; margin-bottom: 16px;
  }
  .about p {
    font-size: 10.5px; line-height: 14px; color: var(--body-text); margin-bottom: 14px;
  }

  .site-footer {
    position: absolute; left: 0; top: 578px; width: 1200px; height: 65px;
    background: var(--footer-bg); border-top: 1px solid var(--divider);
  }
  .footer-brand {
    position: absolute; left: 196px; top: 20px;
    font-family: "Comfortaa", sans-serif; font-size: 20px; color: var(--footer-text);
  }
  .copyright {
    position: absolute; left: 0; right: 0; top: 27px; text-align: center;
    font-size: 10px; color: var(--footer-text);
  }
  .social { position: absolute; left: 900px; top: 18px; display: flex; gap: 10px; }
  .social span { width: 28px; height: 28px; border-radius: 50%; background: var(--icon-bg); }
</style>
</head>
<body>
<div class="page">
  <header class="site-header">
    <div class="brand">
      <span class="brand-dot"></span>
      <span class="brand-name">Velmork Inc.</span>
    </div>
  </header>
  <div class="spotlight"></div>

  <main class="content">
    <svg class="section-ribbon" width="128" height="175" viewBox="0 0 128 175" aria-hidden="false">
      <defs>
        <linearGradient id="ribbonFill" x1="0" y1="0" x2="0" y2="1">
          <stop offset="0" stop-color="var(--ribbon-light)"/>
          <stop offset="1" stop-color="var(--ribbon-dark)"/>
        </linearGradient>
      </defs>
      <path d="M0 0 H126 V150 L63 172 L0 150 Z" fill="url(#ribbonFill)"/>
      <path d="M0 0 H126 V3 H0 Z" fill="rgba(255,255,255,0.35)"/>
      <text x="63" y="110" text-anchor="middle">ABOUT US</text>
    </svg>

    <section class="about">
      <h2>WHAT WE ARE ABOUT</h2>
      <p>Velmork builds dependable technology solutions for growing businesses. Our team plans, designs and delivers software, hosting and support services that keep daily operations running smoothly. We listen first, then shape tools around the way your people already work, so every project stays practical, secure and easy to maintain over the long term.</p>
      <p>From the first consultation to final launch, we guide clients through each stage with clear timelines and honest advice. Our engineers work with cloud platforms, network infrastructure, custom web applications and data systems. We test carefully, document everything and train your staff so that new tools are adopted quickly. After launch we stay close, monitoring performance, applying updates and answering questions whenever help is needed. Many partners have worked with us for years because we treat their goals as our own and measure success by their results.</p>
      <p>We believe good technology should feel simple. That is why our solutions focus on clarity, reliability and value. Whether you need a new website, a stronger network or a smarter way to manage information, Velmork is ready to help you take the next step with confidence.</p>
    </section>
  </main>

  <footer class="site-footer">
    <div class="footer-brand">Velmork Inc</div>
    <div class="copyright">Copyright © 2012 Velmork Inc. All Rights Reserved.</div>
    <div class="social"><span></span><span></span><span></span></div>
  </footer>
</div>
</body>
</html>
```